High value cover design for an A4 ideation pad.

The product is NOT A BOOK.

It's an A4 ideation pad for professionals, designers and creators who handwrite their ideas. Visualise creators like Marcus Tellwind, Owen Prackett and Dale Vorhanek in your mind's eye.

I'm looking for a cover design for the ideation pad. Both front and back.

It should look, feel and convey the following.

--> A handcrafted product experience

--> High value & Elegance

--> Inspiration

Mandatory --> See Uploaded Files --> Files 1, 5 & 6

Target Market(s)

- Designers

-Creative Professionals

- Entrepreneurs

who handwrite their ideas. Visualise creators like Marcus Tellwind, Owen Prackett and Dale Vorhanek in your mind's eye.

Industry/Entity Type

Stationary

Font styles to use
Script
Other font styles liked:
• Calligraphy

Colors
fbed22

Requirements
Must have
• Title text - Amber Lantern

-Text in gold on brown leather background to convey high value for the front cover.

--> High value & Elegance

--> Inspiration

--> Should compel the customers to pick up and own the idea pad
Nice to have
• That's my take but other ideas are welcome
Should not have
• Must not convey

- low value

```html
<!DOCTYPE html>
<html lang="en">
<head>
<meta charset="utf-8">
<title>Amber Lantern — Ideation Pad Cover</title>
<link rel="stylesheet" href="https://fonts.googleapis.com/css2?family=Bebas+Neue&display=swap">
<style>
  :root {
    --stage: #f4f4f3;
    --cover: #353433;
    --gold: #e3b12f;
    --lead-grey: #d9d8d4;
    --wood-cream: #e6dfb6;
    --pencil-yellow: #d9a930;
    --pencil-shade: #b8902c;
  }
  * { margin: 0; padding: 0; box-sizing: border-box; }
  html, body {
    width: 1200px;
    height: 901px;
    overflow: hidden;
    background: var(--stage);
  }
  .canvas {
    position: relative;
    width: 1200px;
    height: 901px;
  }
  .pad-cover {
    position: absolute;
    left: 310px;
    top: 40px;
    width: 580px;
    height: 820px;
    background: var(--cover);
    overflow: hidden;
    box-shadow: 0 10px 30px rgba(0, 0, 0, 0.18);
  }
  .pencil-art {
    position: absolute;
    left: 262px;
    top: 96px;
    width: 196px;
    height: 724px;
    background: linear-gradient(
      to bottom,
      #3a3a3a 0%,
      var(--lead-grey) 8%,
      var(--lead-grey) 52%,
      var(--wood-cream) 60%,
      var(--pencil-yellow) 66%,
      var(--pencil-shade) 100%
    );
    opacity: 0.92;
  }
  .title {
    position: absolute;
    left: 70px;
    top: 300px;
    font-family: "Bebas Neue", "Oswald", sans-serif;
    color: var(--gold);
    line-height: 0.86;
    letter-spacing: 1px;
  }
  .title-top {
    display: block;
    font-size: 104px;
    padding-left: 4px;
  }
  .title-main {
    display: block;
    font-size: 168px;
  }
</style>
</head>
<body>
  <main class="canvas">
    <section class="pad-cover">
      <div class="pencil-art" role="img" aria-label="Illustration of a sharpened yellow pencil pointing upward, its grey marbled tip rising behind the title"></div>
      <h1 class="title">
        <span class="title-top">Amber</span>
        <span class="title-main">Lantern</span>
      </h1>
    </section>
  </main>
</body>
</html>
```